Business Card Design

I need a business card for my resume writing business. I have a logo that Im not keen on anymore so I would like the business card to use my photo instead of a logo. I am for mid career and trades resumes and prefer not to do executive resumes so don't need to aim for exectives. I would like it to be colourful. I like bright sky blue and maybe some pink or purple but primarily bright sky blue. I don't like green and Im keen see a fair bit of white on the card. As I have a photo to go it, it will need to go on a white background.

Target Market(s)

mid range careers. Not executives

Industry/Entity Type

Business

Contact Information for Business Card

Wyn Marchetti
Resume Writer
Clear Path CVs
27 The Lanyard
HARWOOD NSW 2465
wyn@clearpathcvs.com.au
0417362958
www.clearpathcvs.com.au

Requirements
Nice to have
• Maybe colours similar to my website - www.clearpathcvs.com.au but not with any black on it.
Should not have
• No green or dark colours

```html
<!DOCTYPE html>
<html lang="en">
<head>
<meta charset="utf-8">
<title>Clear Path CVs – Business Card</title>
<link href="https://fonts.googleapis.com/css2?family=Roboto:wght@400&family=Arimo:wght@400&family=Handlee&display=swap" rel="stylesheet">
<style>
  :root {
    --page-bg: #eceef0;
    --card-bg: #ffffff;
    --sky: #2fa3e0;
    --sky-light: #8fd3f4;
    --ink: #1c1c1c;
    --photo-top: #f3efeb;
    --photo-bottom: #d9cfc8;
  }
  * { margin: 0; padding: 0; box-sizing: border-box; }
  html, body {
    width: 1200px; height: 1094px; overflow: hidden;
    background: var(--page-bg);
  }
  .card {
    position: absolute; left: 50px; top: 227px;
    width: 1100px; height: 640px;
    background: var(--card-bg);
    box-shadow: 0 6px 24px rgba(0,0,0,.18);
    overflow: hidden;
  }
  .card-shapes { position: absolute; inset: 0; width: 100%; height: 100%; }
  .portrait {
    position: absolute; left: 14px; top: 146px;
    width: 578px; height: 494px;
    border-radius: 240px 240px 0 0;
    background: linear-gradient(180deg, var(--photo-top), var(--photo-bottom));
  }
  .card-title {
    position: absolute; left: 47px; top: 36px;
    font: 400 43px/1 "Roboto", sans-serif; color: var(--ink);
    letter-spacing: -0.3px;
  }
  .brand-name {
    position: absolute; left: 627px; top: 205px;
    font: 400 48px/1 "Handlee", cursive; color: var(--sky);
    letter-spacing: 1px;
  }
  .brand-rule {
    position: absolute; left: 627px; top: 261px;
    width: 413px; height: 3px; background: var(--sky);
  }
  .contact-list { position: absolute; left: 620px; top: 284px; list-style: none; }
  .contact-item {
    display: flex; align-items: flex-start;
    font: 400 25px/31px "Arimo", sans-serif; color: var(--ink);
    margin-bottom: 4px;
  }
  .contact-item svg { width: 34px; height: 30px; margin-right: 33px; flex: none; fill: var(--sky); }
</style>
</head>
<body>
  <div class="card">
    <svg class="card-shapes" viewBox="0 0 825 480" preserveAspectRatio="none" aria-hidden="true">
      <path d="M0,70 C60,230 250,330 420,360 C560,388 700,440 770,480 L0,480 Z" fill="var(--sky-light)"/>
      <path d="M4,52 C60,220 240,322 410,352 C560,378 690,430 760,480" fill="none" stroke="var(--sky)" stroke-width="15"/>
      <path d="M585,0 C680,38 770,88 825,145" fill="none" stroke="var(--sky)" stroke-width="18"/>
    </svg>

    <div class="portrait" role="img" aria-label="Portrait photo of the resume writer"></div>

    <h1 class="card-title">Wyn Marchetti Resume Writer</h1>

    <div class="brand-name">Clear Path CVs</div>
    <div class="brand-rule"></div>

    <ul class="contact-list">
      <li class="contact-item">
        <svg viewBox="0 0 24 24"><path d="M12 2a7 7 0 0 0-7 7c0 5 7 13 7 13s7-8 7-13a7 7 0 0 0-7-7zm0 9.5A2.5 2.5 0 1 1 12 6.5a2.5 2.5 0 0 1 0 5z"/></svg>
        <span>27 The Lanyard<br>HARWOOD NSW 2465</span>
      </li>
      <li class="contact-item">
        <svg viewBox="0 0 24 24"><path d="M2 5h20v14H2z" fill="none" stroke="var(--sky)" stroke-width="1.8"/><path d="M2 5l10 8 10-8" fill="none" stroke="var(--sky)" stroke-width="1.8"/></svg>
        <span>wyn@clearpathcvs.com.au</span>
      </li>
      <li class="contact-item">
        <svg viewBox="0 0 24 24" fill="none" stroke="var(--sky)" stroke-width="1.5"><circle cx="12" cy="12" r="9"/><ellipse cx="12" cy="12" rx="4" ry="9"/><path d="M3 12h18M4.5 7.5h15M4.5 16.5h15"/></svg>
        <span>www.clearpathcvs.com.au</span>
      </li>
      <li class="contact-item">
        <svg viewBox="0 0 24 24"><path d="M3 8c0-2 4-4 9-4s9 2 9 4v2h-5V8H8v2H3z"/><path d="M6 11h12l2 8H4z"/><circle cx="12" cy="15" r="2" fill="#fff"/></svg>
        <span>0417362958</span>
      </li>
    </ul>
  </div>
</body>
</html>
```